Health & Nutrition - Business Cards

Needs to look new-age, simple, and elegant. The cards are for my services/counsel in health and nutrition - which include mind, body, and soul. I would like to see something clean and simple but beautiful. Can have a plain background or with a pattern but I don't want it to take away from my contact details. Therefore, my info can be on the back of the card and a nice front design. I really like the flower of life symbol. The name of my business is called Willow Lantern.

Target Market(s)

Clients - men & women age 20-60. Adults, parents, teachers, sick individuals seeking nutrient counseling and dietary management.

Industry/Entity Type

Nutritionist

Contact Information for Business Card

Tomas Brindle
Cell: 345-582-7046
Email: tbrindle@mailvane.net

Colors
33a6d7
33b8a4
add136
ffffff
5c5c5c
f04a50
fbee3f
cedeed
85cae6

Requirements
Nice to have
• Maybe it can have some sort of sacred geometry as well, but not required. Nice to have the colors that I choose in the project but feel free to come up with your own use of colors. Thanks! =)

```html
<!DOCTYPE html>
<html lang="en">
<head>
<meta charset="utf-8">
<title>Tomas Brindle – Nutritionist</title>
<link rel="stylesheet" href="https://fonts.googleapis.com/css2?family=Della+Respira&family=Kalam:wght@400;700&display=swap">
<style>
  :root {
    --card-green: #add136;
    --accent-red: #f04a50;
    --ink-grey: #5c5c5c;
    --icon-glyph: #add136;
  }
  * { margin: 0; padding: 0; box-sizing: border-box; }
  html, body {
    width: 1200px;
    height: 720px;
    overflow: hidden;
    background: var(--card-green);
  }
  .card {
    position: relative;
    width: 1200px;
    height: 720px;
    background: var(--card-green);
  }
  .owner-name {
    position: absolute;
    top: 52px;
    left: 0;
    width: 1200px;
    text-align: center;
    font-family: "Della Respira", serif;
    font-size: 66px;
    line-height: 1;
    letter-spacing: 1px;
    text-transform: uppercase;
    color: var(--accent-red);
    font-weight: 400;
    -webkit-text-stroke: 1.2px var(--accent-red);
  }
  .owner-role {
    position: absolute;
    top: 128px;
    left: 0;
    width: 1200px;
    text-align: center;
    font-family: "Kalam", cursive;
    font-size: 40px;
    line-height: 1;
    color: var(--ink-grey);
  }
  .contact-row {
    position: absolute;
    left: 351px;
    display: flex;
    align-items: center;
    gap: 14px;
  }
  .contact-row--phone { top: 335px; }
  .contact-row--email { top: 443px; }
  .contact-icon { width: 66px; height: 66px; flex: none; }
  .contact-phone {
    font-family: "Della Respira", serif;
    font-size: 40px;
    color: var(--accent-red);
    -webkit-text-stroke: 1px var(--accent-red);
    letter-spacing: -0.5px;
  }
  .contact-email {
    font-family: "Kalam", cursive;
    font-weight: 700;
    font-size: 40px;
    color: var(--accent-red);
  }
</style>
</head>
<body>
  <main class="card">
    <h1 class="owner-name">Tomas Brindle</h1>
    <p class="owner-role">Nutritionist</p>

    <div class="contact-row contact-row--phone">
      <svg class="contact-icon" viewBox="0 0 66 66" aria-hidden="true">
        <circle cx="33" cy="33" r="32" fill="var(--ink-grey)"/>
        <path d="M22 18c2-1 4-1 5 1l3 6c1 2 0 3-1 4l-2 2c1 4 5 8 9 10l2-2c1-1 3-2 4-1l6 3c2 1 2 3 1 5l-2 3c-2 2-5 2-8 1-9-4-16-11-19-20-1-3 0-6 2-8z" fill="var(--icon-glyph)"/>
      </svg>
      <span class="contact-phone">345-582-7046</span>
    </div>

    <div class="contact-row contact-row--email">
      <svg class="contact-icon" viewBox="0 0 66 66" aria-hidden="true">
        <circle cx="33" cy="33" r="33" fill="var(--ink-grey)"/>
        <rect x="14" y="21" width="38" height="25" fill="var(--icon-glyph)"/>
        <path d="M14 21l19 15 19-15M14 46l14-13M52 46L38 33" fill="none" stroke="var(--ink-grey)" stroke-width="2.2"/>
      </svg>
      <span class="contact-email">tbrindle@mailvane.net</span>
    </div>
  </main>
</body>
</html>
```